Technology Consulting
I need single sided standard sized Business Card [3.5" x 2"]
use something that looks conservative and contemporary
Simple
Mark Delaney
System's Engineer
48 Harrow Lane
mdelaney@quorvalenconsulting.com
http://www.quorvalenconsutling.com
use a font that looks conservative and contemporary

```html
<!DOCTYPE html>
<html lang="en">
<head>
<meta charset="utf-8">
<title>Quorvalen Consulting Stationery</title>
<link rel="stylesheet" href="https://fonts.googleapis.com/css2?family=Montserrat:wght@600&family=Open+Sans:wght@400;600&display=swap">
<style>
  :root {
    --backdrop: #ebe7e1;
    --paper: #ffffff;
    --brand: #1d4f8f;
    --ink: #4a4a4a;
    --muted: #9a9a9a;
    --rule: #c9c9c9;
    --ghost: #eef0f4;
    --label: #3a3a3a;
  }
  * { box-sizing: border-box; margin: 0; padding: 0; }
  html, body { width: 1200px; height: 562px; overflow: hidden; }
  body {
    background: var(--backdrop);
    font-family: "Open Sans", Arial, sans-serif;
    color: var(--ink);
    position: relative;
  }
  .piece-label {
    position: absolute;
    font-size: 8px;
    font-weight: 600;
    color: var(--label);
    text-align: center;
  }
  .sheet {
    position: absolute;
    background: var(--paper);
    box-shadow: 0 1px 4px rgba(0,0,0,.25);
    overflow: hidden;
  }
  .brand {
    display: flex;
    align-items: center;
    gap: 6px;
    font-family: "Montserrat", Arial, sans-serif;
    font-weight: 600;
    color: var(--brand);
    letter-spacing: .04em;
    text-transform: uppercase;
    white-space: nowrap;
  }
  .brand-dot { border-radius: 50%; background: var(--brand); flex: none; }
  .ghost-disc {
    position: absolute;
    border-radius: 50%;
    background: var(--ghost);
  }
  .footer-line {
    position: absolute;
    left: 0; right: 0;
    text-align: center;
    font-size: 4.5px;
    color: var(--muted);
  }

  /* Fax cover */
  .fax { left: 29px; top: 24px; width: 324px; height: 523px; }
  .fax .brand { position: absolute; left: 22px; top: 26px; font-size: 15px; }
  .fax .brand-dot { width: 16px; height: 16px; }
  .fax-title {
    position: absolute; right: 22px; top: 92px;
    font-size: 11px; font-weight: 600; color: var(--label);
  }
  .fax-table {
    position: absolute; left: 22px; top: 106px; width: 280px;
    border-collapse: collapse; font-size: 6px;
  }
  .fax-table td { border: 1px solid var(--rule); height: 14px; padding: 0 4px; }
  .fax-table .key { width: 36px; color: var(--ink); }
  .fax-checks {
    position: absolute; left: 22px; top: 176px; width: 280px;
    display: flex; justify-content: space-between; font-size: 6px;
  }
  .fax-checks span::before {
    content: ""; display: inline-block; width: 6px; height: 6px;
    border: 1px solid var(--muted); margin-right: 3px; vertical-align: -1px;
  }
  .fax .ghost-disc { left: 62px; top: 340px; width: 200px; height: 200px; }
  .fax .footer-line { bottom: 10px; }

  /* Letterhead */
  .letterhead { left: 379px; top: 24px; width: 322px; height: 523px; }
  .letterhead .brand { position: absolute; left: 0; right: 0; top: 26px; justify-content: center; font-size: 15px; }
  .letterhead .brand-dot { width: 16px; height: 16px; }
  .letterhead .ghost-disc { left: 61px; top: 340px; width: 200px; height: 200px; }
  .letterhead .footer-line { bottom: 10px; }

  /* Business cards */
  .card { width: 156px; height: 89px; top: 43px; }
  .card-front { left: 785px; }
  .card-front .brand { position: absolute; left: 10px; top: 12px; font-size: 9px; gap: 4px; }
  .card-front .brand-dot { width: 10px; height: 10px; }
  .card-contact { position: absolute; left: 10px; top: 38px; font-size: 4.6px; line-height: 1.5; }
  .card-contact .name { font-weight: 600; font-size: 5.5px; color: var(--brand); }
  .card-front .ghost-disc { right: -20px; bottom: -40px; width: 90px; height: 90px; }
  .card-back { left: 950px; }
  .card-back .brand { position: absolute; left: 0; right: 0; top: 37px; justify-content: center; font-size: 11px; }
  .card-back .brand-dot { width: 12px; height: 12px; }

  /* Envelopes */
  .envelope { left: 785px; width: 391px; height: 192px; }
  .envelope-front { top: 144px; }
  .envelope-front .brand { position: absolute; left: 16px; top: 14px; font-size: 13px; }
  .envelope-front .brand-dot { width: 14px; height: 14px; }
  .envelope-front .return-address { position: absolute; left: 36px; top: 34px; font-size: 4.5px; color: var(--ink); }
  .envelope-front .ghost-disc { left: 120px; top: 96px; width: 150px; height: 150px; }
  .envelope-back { top: 355px; }
  .envelope-back svg { position: absolute; inset: 0; }
  .envelope-back .brand { position: absolute; left: 0; right: 0; top: 112px; justify-content: center; font-size: 9px; gap: 4px; }
  .envelope-back .brand-dot { width: 10px; height: 10px; }
</style>
</head>
<body>

  <div class="piece-label" style="left:29px;top:10px;width:324px;">Fax Cover</div>
  <section class="sheet fax">
    <div class="brand"><span class="brand-dot"></span>Quorvalen</div>
    <div class="fax-title">FAX</div>
    <table class="fax-table">
      <tr><td class="key">To:</td><td></td><td class="key">From:</td><td></td></tr>
      <tr><td class="key">Fax:</td><td></td><td class="key">Pages:</td><td></td></tr>
      <tr><td class="key">Phone:</td><td></td><td class="key">Date:</td><td></td></tr>
      <tr><td class="key">Re:</td><td></td><td class="key">CC:</td><td></td></tr>
    </table>
    <div class="fax-checks">
      <span>Urgent</span><span>For Review</span><span>Please Comment</span><span>Please Reply</span><span>Please Recycle</span>
    </div>
    <div class="ghost-disc"></div>
    <div class="footer-line">48 Harrow Lane &nbsp;|&nbsp; mdelaney@quorvalenconsulting.com &nbsp;|&nbsp; http://www.quorvalenconsutling.com</div>
  </section>

  <div class="piece-label" style="left:379px;top:10px;width:322px;">Letterhead</div>
  <section class="sheet letterhead">
    <div class="brand"><span class="brand-dot"></span>Quorvalen</div>
    <div class="ghost-disc"></div>
    <div class="footer-line">48 Harrow Lane &nbsp;|&nbsp; mdelaney@quorvalenconsulting.com &nbsp;|&nbsp; http://www.quorvalenconsutling.com</div>
  </section>

  <div class="piece-label" style="left:785px;top:30px;width:156px;">Business Card (Front)</div>
  <section class="sheet card card-front">
    <div class="brand"><span class="brand-dot"></span>Quorvalen</div>
    <div class="card-contact">
      <div class="name">Mark Delaney</div>
      <div>System's Engineer</div>
      <div>48 Harrow Lane</div>
      <div>mdelaney@quorvalenconsulting.com</div>
      <div>http://www.quorvalenconsutling.com</div>
    </div>
    <div class="ghost-disc"></div>
  </section>

  <div class="piece-label" style="left:950px;top:30px;width:156px;">Business Card (Back)</div>
  <section class="sheet card card-back">
    <div class="brand"><span class="brand-dot"></span>Quorvalen</div>
  </section>

  <div class="piece-label" style="left:785px;top:133px;width:391px;">Envelope (Front)</div>
  <section class="sheet envelope envelope-front">
    <div class="brand"><span class="brand-dot"></span>Quorvalen</div>
    <div class="return-address">48 Harrow Lane</div>
    <div class="ghost-disc"></div>
  </section>

  <div class="piece-label" style="left:785px;top:343px;width:391px;">Envelope (Back)</div>
  <section class="sheet envelope envelope-back">
    <svg width="391" height="192" viewBox="0 0 391 192" aria-hidden="true">
      <path d="M0 0 L170 100 Q195 112 220 100 L391 0" fill="none" stroke="#c9c9c9" stroke-width="1"/>
      <path d="M0 192 L160 118 M391 192 L230 118" fill="none" stroke="#dcdcdc" stroke-width="1"/>
    </svg>
    <div class="brand"><span class="brand-dot"></span>Quorvalen</div>
  </section>

</body>
</html>
```